Craft oriented film company needs a Business Card design

Hi all,
We're a 2-man band film company in New Zealand called Brindle Pictures. We're good honest blokes, who are very passionate about the craft of film making. I've attached our current logo which has a bit of a crafty/artisan feel that we like. Feel free to use it - or throw the baby out with the bathwater and start again..... you never know, you might inspire a complete brand re-work.

In any case, the vibe we want to give out is that we are solid, dependable and no bullshit - but without compromising creative excellence and being in the now. We like the 'Brooklyn' artisan style of work.

Preferably single sided.

We need the standard stuff:
Name, job title, cellphone, email address and physical address (this can be smaller if you like - street, suburb, city & zip, country [if you want])

Check out our website to learn more about us: brindlepictures.example

Target Market(s)

Brand marketers and advertising agency creatives looking for video production.

Requirements
Should not have
• Nothing flashy or too 'futuristic', we want it to feel grounded and real. A limited colour palette is preferred.
We don't want any film reels or cameras or anything obvious like that.

```html
<!DOCTYPE html>
<html lang="en">
<head>
<meta charset="utf-8">
<title>Brindle Pictures — Business Card</title>
<link rel="stylesheet" href="https://fonts.googleapis.com/css2?family=Josefin+Sans:wght@400;600&family=Playball&display=swap">
<style>
  :root {
    --backdrop: #d9d6d0;
    --card: #141414;
    --silver: #d6d4ce;
    --silver-soft: #b9b7b1;
  }
  * { margin: 0; padding: 0; box-sizing: border-box; }
  html, body {
    width: 1200px;
    height: 768px;
    overflow: hidden;
    background: var(--backdrop);
  }
  .card {
    position: absolute;
    left: 180px;
    top: 144px;
    width: 840px;
    height: 480px;
    background: var(--card);
    color: var(--silver);
    font-family: "Josefin Sans", sans-serif;
    box-shadow: 0 10px 30px rgba(0,0,0,0.25);
  }
  .person-name {
    position: absolute;
    left: 52px;
    top: 48px;
    font-family: "Playball", cursive;
    font-size: 60px;
    font-weight: 400;
    letter-spacing: 1px;
    line-height: 1;
  }
  .person-role {
    position: absolute;
    left: 100px;
    top: 122px;
    font-size: 22px;
    letter-spacing: 7px;
  }
  .rule-set {
    position: absolute;
    left: 52px;
    top: 190px;
    width: 480px;
    height: 120px;
  }
  .brand-seal {
    position: absolute;
    left: 540px;
    top: 70px;
    width: 250px;
    height: 250px;
    border: 3px solid var(--silver);
    border-radius: 50%;
    display: flex;
    align-items: center;
    justify-content: center;
    text-align: center;
  }
  .brand-name {
    font-size: 34px;
    font-weight: 600;
    letter-spacing: 2px;
    line-height: 1.15;
    text-transform: uppercase;
  }
  .contact {
    position: absolute;
    left: 52px;
    top: 318px;
    font-size: 19px;
    letter-spacing: 1.5px;
    line-height: 30px;
    text-transform: uppercase;
    font-style: normal;
  }
  .contact .company {
    font-family: "Playball", cursive;
    font-size: 24px;
    text-transform: none;
    letter-spacing: 0.5px;
  }
  .contact .label {
    display: inline-block;
    width: 18px;
    font-family: "Playball", cursive;
    text-transform: none;
    font-size: 20px;
  }
  .contact .gap { display: inline-block; width: 38px; }
  .divider {
    position: absolute;
    left: 556px;
    top: 346px;
    width: 2px;
    height: 96px;
    background: var(--silver-soft);
  }
  .services {
    position: absolute;
    right: 54px;
    top: 338px;
    list-style: none;
    text-align: right;
    font-family: "Playball", cursive;
    font-size: 21px;
    line-height: 28px;
    color: var(--silver);
  }
</style>
</head>
<body>
  <article class="card">
    <h1 class="person-name">Callum Reid</h1>
    <p class="person-role">DIRECTOR</p>

    <svg class="rule-set" viewBox="0 0 480 120" aria-hidden="true">
      <g stroke="#d6d4ce" stroke-width="2">
        <line x1="150" y1="38" x2="160" y2="38"/>
        <line x1="185" y1="38" x2="195" y2="38"/>
        <line x1="225" y1="38" x2="260" y2="38"/>
        <line x1="270" y1="38" x2="320" y2="38"/>
        <line x1="335" y1="38" x2="345" y2="38"/>
        <line x1="360" y1="38" x2="420" y2="38"/>
        <line x1="0" y1="92" x2="40" y2="92"/>
        <line x1="55" y1="92" x2="105" y2="92"/>
        <line x1="112" y1="92" x2="140" y2="92"/>
        <line x1="150" y1="92" x2="160" y2="92"/>
      </g>
    </svg>

    <div class="brand-seal">
      <p class="brand-name">Brindle<br>Pictures</p>
    </div>

    <address class="contact">
      <div><span class="company">Brindle Pictures,</span> Kowhai Bay, NZ 4820</div>
      <div><span class="label">p</span>+00 812 450 117<span class="gap"></span><span class="label">m</span>0912 604 385</div>
      <div><span class="label">w</span>brindlepictures.example</div>
      <div><span class="label">e</span>studio@brindlepictures.example</div>
    </address>

    <div class="divider"></div>

    <ul class="services">
      <li>Commercials</li>
      <li>Music Videos</li>
      <li>Online Videos</li>
      <li>B2B</li>
    </ul>
  </article>
</body>
</html>
```